Stylish Business Cards Wanted

- DOUBLE SIDED Design Required -

High end, edgy cards for a corporate and personal stylist. Must include logo,
Name: Belinda Marsh
Title: Director and Stylist
telephone : +61 8 8417 2950
email: belinda@thewardrobeledger.com
website: thewardrobeledger.com
Tag: Corporate Workwear & Uniform Specialist | Personal Stylist
Would like nice icons for telephone, email, website

Target Market(s)

Businesses wanting stylish uniforms, people wanting stylish wardrobes

Industry/Entity Type

Corporate Workwear Stylist

Contact Information for Business Card

I would like black, white and gold foiling incorporated in the design - possibly a touch of the other colours on my branding guide attached Name: Belinda Marsh Title: Director and Stylist telephone : +61 8 8417 2950 email: belinda@thewardrobeledger.com website: thewardrobeledger.com Tag: Corporate Workwear & Uniform Specialist | Personal Stylist Would like nice icons for telephone, email, website

Font styles to use
Other font styles liked:
• Raleway

Colors

Designer to choose colors to be used in the design.

Requirements
Must have
• Gold foil accents

```html
<!DOCTYPE html>
<html lang="en">
<head>
<meta charset="utf-8">
<title>The Wardrobe Ledger – Business Card</title>
<link href="https://fonts.googleapis.com/css2?family=Dancing+Script:wght@500&family=Raleway:wght@600&family=Roboto:wght@400&display=swap" rel="stylesheet">
<style>
  :root {
    --backdrop: #2b2b2d;
    --card: #fbfbfa;
    --gold: #e3b85a;
    --gold-deep: #c9982f;
    --navy: #1b2140;
    --ink: #1d1f2a;
  }
  * { box-sizing: border-box; margin: 0; padding: 0; }
  html, body { width: 799px; height: 1200px; overflow: hidden; }
  body {
    background: var(--backdrop);
    font-family: "Roboto", Arial, sans-serif;
    position: relative;
  }
  .card {
    position: absolute;
    left: 80px;
    width: 640px;
    height: 370px;
    background: var(--card);
    border-radius: 24px;
    overflow: hidden;
  }
  .card--front { top: 120px; }
  .card--back { top: 700px; }

  .front-wordmark {
    position: absolute;
    inset: 0;
    display: flex;
    align-items: center;
    justify-content: center;
    gap: 16px;
    font-family: "Raleway", Arial, sans-serif;
    font-weight: 600;
    font-size: 46px;
    color: var(--gold-deep);
    letter-spacing: 0.5px;
  }
  .front-wordmark .mark-dot {
    width: 18px; height: 18px; border-radius: 50%;
    background: var(--gold-deep);
  }

  .contact-block { position: absolute; left: 48px; top: 56px; }
  .holder-name {
    font-family: "Dancing Script", cursive;
    font-weight: 500;
    font-size: 36px;
    color: var(--gold);
    line-height: 1;
  }
  .holder-title { font-size: 15px; color: var(--ink); margin-top: 6px; }
  .contact-list { list-style: none; margin-top: 20px; }
  .contact-list li {
    display: flex; align-items: center; gap: 12px;
    font-size: 16px; color: var(--ink); height: 26px;
  }
  .contact-list svg { width: 15px; height: 15px; flex: none; }

  .back-wordmark {
    position: absolute;
    right: 48px; top: 150px;
    display: flex; align-items: center; gap: 12px;
    font-family: "Raleway", Arial, sans-serif;
    font-weight: 600;
    font-size: 28px;
    line-height: 1.15;
    color: var(--navy);
  }
  .back-wordmark .mark-square { width: 12px; height: 12px; background: var(--navy); flex: none; }
  .back-wordmark .mark-text { display: block; }

  .tag-band { position: absolute; left: 0; bottom: 0; width: 640px; height: 92px; }
  .tagline {
    position: absolute; left: 0; right: 0; bottom: 28px;
    text-align: center; font-size: 16px; color: var(--ink);
  }
</style>
</head>
<body>
  <section class="card card--front">
    <div class="front-wordmark"><span class="mark-dot"></span>The Wardrobe Ledger</div>
  </section>

  <section class="card card--back">
    <div class="contact-block">
      <h1 class="holder-name">Belinda Marsh</h1>
      <p class="holder-title">Director and Stylist</p>
      <ul class="contact-list">
        <li>
          <svg viewBox="0 0 16 16" fill="none" stroke="var(--gold-deep)" stroke-width="1.3"><circle cx="8" cy="8" r="7"/><path d="M5.6 4.6l1.2 1.6-.7 1a4.5 4.5 0 0 0 2.3 2.3l1-.7 1.6 1.2-.6 1.2C7.5 11 5 8.5 4.4 5.2z" fill="var(--gold-deep)" stroke="none"/></svg>
          +61 8 8417 2950
        </li>
        <li>
          <svg viewBox="0 0 16 16" fill="none" stroke="var(--gold-deep)" stroke-width="1.3"><rect x="1.5" y="3.5" width="13" height="9" rx="1"/><path d="M1.8 4l6.2 4.8L14.2 4"/></svg>
          belinda@thewardrobeledger.com
        </li>
        <li>
          <svg viewBox="0 0 16 16" fill="none" stroke="var(--gold-deep)" stroke-width="1.2"><circle cx="8" cy="8" r="6.5"/><ellipse cx="8" cy="8" rx="3" ry="6.5"/><path d="M1.5 8h13M2.5 5h11M2.5 11h11"/></svg>
          www.thewardrobeledger.com
        </li>
      </ul>
    </div>

    <div class="back-wordmark"><span class="mark-square"></span><span class="mark-text">The Wardrobe<br>Ledger</span></div>

    <svg class="tag-band" viewBox="0 0 640 92" preserveAspectRatio="none">
      <rect x="0" y="80" width="640" height="12" fill="var(--navy)"/>
      <path d="M0 92 V30 Q0 8 28 8 H590 Q608 8 612 26 L624 92 Z" fill="var(--gold)"/>
    </svg>
    <p class="tagline">Corporate Workwear &amp; Uniform Specialist &nbsp;|&nbsp; Personal Stylist</p>
  </section>
</body>
</html>
```